School Fundraising Flyer Marlowe Ridge Falcons

We want to create a flyer that will be handed out by students to sell t-shirts. Users will be instructed to go to a webpage url http://brextonprints.example/fundraising/marlowe/ (or qr code) to view items for sale. There will be 12 products to be sold. The flyer will be 8.5 x 11" unfolded sheet. It will be front and back, full color both sides. The school mascot is a native american Indian chief, and the school color are royal blue, and yellow. Will require Indesign File (source file) at completion

Target Market(s)

School age kids, and parents

Industry/Entity Type

Retail

Font styles to use
Sans Serif

Colors
0355a3
fbed22
ffffff

Requirements
Must have
• 12 placeholders, link to website, qr codes.
Nice to have
• Mascot theme
Should not have
• no profanities

```html
<!DOCTYPE html>
<html lang="en">
<head>
<meta charset="utf-8">
<title>Marlowe Ridge Falcons Fundraising Flyer</title>
<link rel="stylesheet" href="https://fonts.googleapis.com/css2?family=Montserrat:wght@600;700;800&display=swap">
<style>
  :root {
    --stage: #bdbdbd;
    --paper: #ffffff;
    --royal: #0355a3;
    --royal-light: #2f6fc0;
    --shirt: #3a63c0;
    --yellow: #fbed22;
    --pink: #e48ea3;
    --pink-light: #eeb0bf;
    --pink-deep: #d4677f;
    --rose: #d6323f;
  }
  * { box-sizing: border-box; }
  html, body {
    margin: 0;
    width: 1200px;
    height: 1200px;
    overflow: hidden;
    background: var(--stage);
    font-family: "Montserrat", sans-serif;
  }
  .flyer {
    position: absolute;
    left: 165px;
    top: 40px;
    width: 870px;
    height: 1120px;
    border: 20px solid var(--paper);
    background: var(--royal);
    overflow: hidden;
    box-shadow: 0 10px 18px rgba(0,0,0,0.35);
  }
  .flyer__top {
    position: absolute;
    left: 0; top: 0;
    width: 830px; height: 551px;
    background:
      radial-gradient(circle at 6% 10%, rgba(214,50,63,0.7) 0 40px, transparent 80px),
      radial-gradient(circle at 94% 6%, rgba(214,50,63,0.6) 0 36px, transparent 72px),
      linear-gradient(160deg, var(--pink-light) 0%, var(--pink) 60%, var(--pink-deep) 100%);
  }
  .flyer__bottom {
    position: absolute;
    left: 0; top: 551px;
    width: 830px; height: 529px;
    background: radial-gradient(ellipse at 35% 50%, var(--royal-light) 0%, var(--royal) 70%);
  }
  .hero-photo {
    position: absolute;
    left: 60px; top: 40px;
    width: 360px; height: 511px;
    border-radius: 150px 150px 0 0;
    background: linear-gradient(180deg, #c98a86 0%, #6d4d5a 22%, var(--shirt) 34%, #3157b0 85%, #2a3550 100%);
  }
  .headline {
    position: absolute;
    left: 460px; top: 44px;
    width: 340px;
    color: var(--royal);
  }
  .headline__school {
    margin: 0;
    font-weight: 800;
    font-size: 44px;
    line-height: 1.02;
    text-transform: uppercase;
  }
  .headline__tag {
    margin: 12px 0 0;
    display: inline-block;
    padding: 6px 12px;
    background: var(--royal);
    color: var(--yellow);
    font-weight: 700;
    font-size: 17px;
    letter-spacing: 0.04em;
    text-transform: uppercase;
  }
  .scan {
    position: absolute;
    left: 460px; top: 230px;
    display: flex;
    align-items: center;
    gap: 16px;
  }
  .scan__code {
    width: 104px; height: 104px;
    background: var(--paper);
    border: 8px solid var(--paper);
    outline: 3px solid var(--royal);
    display: flex;
    align-items: center;
    justify-content: center;
    color: var(--royal);
    font-weight: 700;
    font-size: 13px;
    text-align: center;
  }
  .scan__text {
    margin: 0;
    color: var(--royal);
    font-weight: 700;
    font-size: 17px;
    line-height: 1.3;
    width: 190px;
  }
  .brand {
    position: absolute;
    left: 460px; top: 372px;
    display: flex;
    align-items: center;
    gap: 10px;
  }
  .brand__dot {
    width: 22px; height: 22px;
    border-radius: 50%;
    background: var(--royal);
  }
  .brand__name {
    font-weight: 800;
    font-size: 24px;
    color: var(--royal);
    white-space: nowrap;
  }
  .thumb {
    position: absolute;
    top: 445px;
    width: 212px; height: 212px;
    border-radius: 50%;
    border: 5px solid var(--yellow);
    box-shadow: 0 0 0 3px var(--paper);
  }
  .thumb--one { left: 48px; background: linear-gradient(180deg, #4f7a38 0%, #3b6a2e 45%, var(--shirt) 46%, #2e58ad 100%); }
  .thumb--two { left: 309px; background: linear-gradient(180deg, #b9c58c 0%, #93a86c 45%, var(--shirt) 46%, #3263b8 100%); }
  .thumb--three { left: 570px; background: linear-gradient(180deg, #8aa0c4 0%, #5a77a8 45%, var(--shirt) 46%, #3a66b4 100%); }
  .group-photo {
    position: absolute;
    left: 30px; top: 690px;
    width: 380px; height: 320px;
    border-radius: 110px 110px 0 0;
    background:
      linear-gradient(90deg, transparent 35%, #e6e43a 35% 65%, transparent 65%),
      linear-gradient(180deg, #4a73c9 0%, #3560b8 75%, #7c97c4 100%);
  }
  .catalog {
    position: absolute;
    left: 440px; top: 686px;
    width: 360px;
  }
  .catalog__title {
    margin: 0 0 10px;
    color: var(--paper);
    font-weight: 800;
    font-size: 19px;
    text-transform: uppercase;
  }
  .catalog__title span { color: var(--yellow); }
  .catalog__grid {
    display: grid;
    grid-template-columns: repeat(4, 82px);
    gap: 10px;
  }
  .product {
    height: 90px;
    background: var(--paper);
    border: 3px solid var(--yellow);
    display: flex;
    flex-direction: column;
    align-items: center;
    justify-content: flex-end;
    padding-bottom: 6px;
    color: var(--royal);
    font-weight: 700;
    font-size: 12px;
  }
  .product__swatch {
    width: 46px; height: 46px;
    margin-bottom: 6px;
    border-radius: 6px;
    background: var(--royal);
  }
  .product--yellow .product__swatch { background: var(--yellow); border: 2px solid var(--royal); }
  .url-band {
    position: absolute;
    left: 0; top: 1024px;
    width: 830px; height: 56px;
    background: var(--yellow);
    display: flex;
    align-items: center;
    justify-content: center;
    gap: 12px;
    color: var(--royal);
    font-size: 19px;
  }
  .url-band__label { font-weight: 800; text-transform: uppercase; }
  .url-band__link { font-weight: 700; }
</style>
</head>
<body>
  <main class="flyer">
    <div class="flyer__top"></div>
    <div class="flyer__bottom"></div>

    <div class="hero-photo" role="img" aria-label="Photo of a student wearing a royal blue Marlowe Ridge Falcons t-shirt against a pink wall with red paper roses"></div>

    <header class="headline">
      <h1 class="headline__school">Marlowe Ridge Falcons</h1>
      <p class="headline__tag">Spirit Wear Fundraiser</p>
    </header>

    <div class="scan">
      <div class="scan__code" role="img" aria-label="QR code linking to the fundraising store">QR CODE</div>
      <p class="scan__text">Scan to shop all 12 shirts online</p>
    </div>

    <div class="brand">
      <span class="brand__dot"></span>
      <span class="brand__name">brextonprints.example</span>
    </div>

    <div class="thumb thumb--one" role="img" aria-label="Photo of a student in a blue falcons t-shirt in front of ivy"></div>
    <div class="thumb thumb--two" role="img" aria-label="Photo of a student in sunglasses wearing a blue falcons t-shirt outdoors"></div>
    <div class="thumb thumb--three" role="img" aria-label="Photo of a student in a blue falcons t-shirt beside a car"></div>

    <div class="group-photo" role="img" aria-label="Photo of three students wearing blue and yellow Marlowe Ridge Falcons t-shirts"></div>

    <section class="catalog">
      <h2 class="catalog__title">Choose from <span>12 styles</span></h2>
      <div class="catalog__grid">
        <div class="product"><span class="product__swatch"></span>Style 01</div>
        <div class="product product--yellow"><span class="product__swatch"></span>Style 02</div>
        <div class="product"><span class="product__swatch"></span>Style 03</div>
        <div class="product product--yellow"><span class="product__swatch"></span>Style 04</div>
        <div class="product product--yellow"><span class="product__swatch"></span>Style 05</div>
        <div class="product"><span class="product__swatch"></span>Style 06</div>
        <div class="product product--yellow"><span class="product__swatch"></span>Style 07</div>
        <div class="product"><span class="product__swatch"></span>Style 08</div>
        <div class="product"><span class="product__swatch"></span>Style 09</div>
        <div class="product product--yellow"><span class="product__swatch"></span>Style 10</div>
        <div class="product"><span class="product__swatch"></span>Style 11</div>
        <div class="product product--yellow"><span class="product__swatch"></span>Style 12</div>
      </div>
    </section>

    <footer class="url-band">
      <span class="url-band__label">Shop now:</span>
      <span class="url-band__link">http://brextonprints.example/fundraising/marlowe/</span>
    </footer>
  </main>
</body>
</html>
```